Logo & Visitenkarte für Gesundheit
Zielgruppe
Gesundheitsprodukte
Ernährungsberatung
Aufgabenstellung
nicht spezifisch Logo mit Essen und Trinken. Eher ein allgemeines Logo für Gesundheit

```html
<!DOCTYPE html>
<html lang="de">
<head>
<meta charset="utf-8">
<title>Vitalgrund – Visitenkarten</title>
<link href="https://fonts.googleapis.com/css2?family=Roboto:wght@400;500;700&display=swap" rel="stylesheet">
<style>
  :root{
    --bg:#e6e7e9;
    --teal-dark:#1b6370;
    --teal:#23777f;
    --cream:#f9e2b8;
    --navy:#0f4a58;
    --lime:#b5c61f;
    --white:#ffffff;
  }
  *{box-sizing:border-box;margin:0;padding:0}
  html,body{width:1200px;height:750px;overflow:hidden;background:var(--bg);font-family:"Roboto",Arial,sans-serif}
  .sheet{position:relative;width:1200px;height:750px}
  .card{position:absolute;width:267px;height:173px}
  .front{display:flex;flex-direction:column;align-items:center;justify-content:center}
  .front--dark{background:var(--teal-dark)}
  .front--teal{background:var(--teal)}
  .front--cream{background:var(--cream)}
  .brand-mark{display:flex;align-items:center;gap:8px;margin-top:-12px}
  .brand-dot{width:16px;height:16px;border-radius:50%;background:var(--lime)}
  .brand-name{font-weight:700;font-size:24px;color:var(--lime);letter-spacing:.5px}
  .front--cream .brand-name{color:var(--navy)}
  .front--cream .brand-dot{background:var(--navy)}
  .front-url{position:absolute;bottom:10px;left:0;right:0;text-align:center;font-size:6.5px;font-weight:500;color:var(--white)}
  .front--cream .front-url{color:var(--navy)}

  .back{background:var(--white)}
  .back-logo{position:absolute;right:14px;top:20px;display:flex;align-items:center;gap:6px}
  .back-logo .brand-dot{width:11px;height:11px;background:var(--navy)}
  .back-logo .brand-name{font-size:19px;color:var(--lime)}
  .person{position:absolute;left:14px;top:82px;color:var(--navy)}
  .person-name{font-weight:700;font-size:11.5px;line-height:1}
  .person-role{font-size:8.5px;margin-top:2px}
  .contact-band{position:absolute;left:0;right:0;top:110px;height:48px;color:var(--white);font-size:8px}
  .band--dark{background:var(--teal-dark)}
  .band--teal{background:var(--teal)}
  .band--cream{background:var(--cream);color:var(--navy)}
  .address{position:absolute;left:14px;top:10px;line-height:10.5px}
  .contacts{position:absolute;left:131px;top:5px;list-style:none}
  .contacts li{display:flex;align-items:center;gap:7px;height:13px}
  .contacts svg{width:10px;height:10px;flex:none}
</style>
</head>
<body>
<div class="sheet">

  <!-- fronts -->
  <section class="card front front--dark" style="left:48px;top:209px">
    <div class="brand-mark"><span class="brand-dot"></span><span class="brand-name">Vitalgrund</span></div>
    <p class="front-url">www.vitalgrund.de</p>
  </section>
  <section class="card front front--teal" style="left:331px;top:209px">
    <div class="brand-mark"><span class="brand-dot"></span><span class="brand-name">Vitalgrund</span></div>
    <p class="front-url">www.vitalgrund.de</p>
  </section>
  <section class="card front front--cream" style="left:617px;top:209px">
    <div class="brand-mark"><span class="brand-dot"></span><span class="brand-name">Vitalgrund</span></div>
    <p class="front-url">www.vitalgrund.de</p>
  </section>
  <section class="card front front--cream" style="left:900px;top:209px">
    <div class="brand-mark"><span class="brand-dot"></span><span class="brand-name">Vitalgrund</span></div>
    <p class="front-url">www.vitalgrund.de</p>
  </section>

  <!-- backs -->
  <section class="card back" style="left:48px;top:436px">
    <div class="back-logo"><span class="brand-dot"></span><span class="brand-name">Vitalgrund</span></div>
    <div class="person"><p class="person-name">MAX MUSTERMAN</p><p class="person-role">Function</p></div>
    <div class="contact-band band--dark">
      <p class="address">Streetnumber 00<br>City name</p>
      <ul class="contacts">
        <li><svg viewBox="0 0 10 10"><path d="M3 1 L4.5 3 L3.5 4.5 Q4.5 6.5 6 7 L7 6 L9 7.5 L8 9 Q3 9 1.5 2.5 Z" fill="currentColor"/></svg>000000000000</li>
        <li><svg viewBox="0 0 10 10"><rect x="0.7" y="2" width="8.6" height="6" fill="none" stroke="currentColor" stroke-width="1"/><path d="M0.7 2 L5 5.5 L9.3 2 M0.7 8 L4 5 M9.3 8 L6 5" fill="none" stroke="currentColor" stroke-width="0.9"/></svg>info@gesundzeit-beratung.de</li>
        <li><svg viewBox="0 0 10 10" fill="none" stroke="currentColor" stroke-width="0.8"><circle cx="5" cy="5" r="4.3"/><ellipse cx="5" cy="5" rx="2" ry="4.3"/><path d="M0.7 5 H9.3 M1.5 2.8 H8.5 M1.5 7.2 H8.5"/></svg>www.gesundzeit-beratung.de</li>
      </ul>
    </div>
  </section>

  <section class="card back" style="left:332px;top:436px">
    <div class="back-logo"><span class="brand-dot"></span><span class="brand-name">Vitalgrund</span></div>
    <div class="person"><p class="person-name">MAX MUSTERMAN</p><p class="person-role">Function</p></div>
    <div class="contact-band band--teal">
      <p class="address">Streetnumber 00<br>City name</p>
      <ul class="contacts">
        <li><svg viewBox="0 0 10 10"><path d="M3 1 L4.5 3 L3.5 4.5 Q4.5 6.5 6 7 L7 6 L9 7.5 L8 9 Q3 9 1.5 2.5 Z" fill="currentColor"/></svg>000000000000</li>
        <li><svg viewBox="0 0 10 10"><rect x="0.7" y="2" width="8.6" height="6" fill="none" stroke="currentColor" stroke-width="1"/><path d="M0.7 2 L5 5.5 L9.3 2 M0.7 8 L4 5 M9.3 8 L6 5" fill="none" stroke="currentColor" stroke-width="0.9"/></svg>info@gesundzeit-beratung.de</li>
        <li><svg viewBox="0 0 10 10" fill="none" stroke="currentColor" stroke-width="0.8"><circle cx="5" cy="5" r="4.3"/><ellipse cx="5" cy="5" rx="2" ry="4.3"/><path d="M0.7 5 H9.3 M1.5 2.8 H8.5 M1.5 7.2 H8.5"/></svg>www.gesundzeit-beratung.de</li>
      </ul>
    </div>
  </section>

  <section class="card back" style="left:617px;top:436px">
    <div class="back-logo"><span class="brand-dot"></span><span class="brand-name">Vitalgrund</span></div>
    <div class="person"><p class="person-name">MAX MUSTERMAN</p><p class="person-role">Function</p></div>
    <div class="contact-band band--cream">
      <p class="address">Streetnumber 00<br>City name</p>
      <ul class="contacts">
        <li><svg viewBox="0 0 10 10"><path d="M3 1 L4.5 3 L3.5 4.5 Q4.5 6.5 6 7 L7 6 L9 7.5 L8 9 Q3 9 1.5 2.5 Z" fill="currentColor"/></svg>000000000000</li>
        <li><svg viewBox="0 0 10 10"><rect x="0.7" y="2" width="8.6" height="6" fill="none" stroke="currentColor" stroke-width="1"/><path d="M0.7 2 L5 5.5 L9.3 2 M0.7 8 L4 5 M9.3 8 L6 5" fill="none" stroke="currentColor" stroke-width="0.9"/></svg>info@gesundzeit-beratung.de</li>
        <li><svg viewBox="0 0 10 10" fill="none" stroke="currentColor" stroke-width="0.8"><circle cx="5" cy="5" r="4.3"/><ellipse cx="5" cy="5" rx="2" ry="4.3"/><path d="M0.7 5 H9.3 M1.5 2.8 H8.5 M1.5 7.2 H8.5"/></svg>www.gesundzeit-beratung.de</li>
      </ul>
    </div>
  </section>

  <section class="card back" style="left:901px;top:436px">
    <div class="back-logo"><span class="brand-dot"></span><span class="brand-name">Vitalgrund</span></div>
    <div class="person"><p class="person-name">MAX MUSTERMAN</p><p class="person-role">Function</p></div>
    <div class="contact-band band--cream">
      <p class="address">Streetnumber 00<br>City name</p>
      <ul class="contacts">
        <li><svg viewBox="0 0 10 10"><path d="M3 1 L4.5 3 L3.5 4.5 Q4.5 6.5 6 7 L7 6 L9 7.5 L8 9 Q3 9 1.5 2.5 Z" fill="currentColor"/></svg>000000000000</li>
        <li><svg viewBox="0 0 10 10"><rect x="0.7" y="2" width="8.6" height="6" fill="none" stroke="currentColor" stroke-width="1"/><path d="M0.7 2 L5 5.5 L9.3 2 M0.7 8 L4 5 M9.3 8 L6 5" fill="none" stroke="currentColor" stroke-width="0.9"/></svg>info@gesundzeit-beratung.de</li>
        <li><svg viewBox="0 0 10 10" fill="none" stroke="currentColor" stroke-width="0.8"><circle cx="5" cy="5" r="4.3"/><ellipse cx="5" cy="5" rx="2" ry="4.3"/><path d="M0.7 5 H9.3 M1.5 2.8 H8.5 M1.5 7.2 H8.5"/></svg>www.gesundzeit-beratung.de</li>
      </ul>
    </div>
  </section>

</div>
</body>
</html>
```